Refresh of graphic design for existing website

We would like to refresh our website. Please see the attached design specifications.

Industry/Entity Type

Graphic Design

```html
<!DOCTYPE html>
<html lang="en">
<head>
<meta charset="utf-8">
<title>Gearline Tool Guild</title>
<link href="https://fonts.googleapis.com/css2?family=Open+Sans:wght@400;600;700&family=PT+Serif:wght@400;700&display=swap" rel="stylesheet">
<style>
:root{
  --teal:#1f8f8a;
  --green:#2a9a6a;
  --green-dark:#1f7a52;
  --ink:#2b2b2b;
  --muted:#6b6b6b;
  --rule:#d6d6d6;
  --nav:#1c1c1c;
  --nav-active:#3a3a3a;
  --footer:#222222;
  --footer-base:#141414;
  --footer-text:#9a9a9a;
  --link:#4aa3d8;
  --blue:#1c6fb3;
  --white:#ffffff;
}
*{box-sizing:border-box;margin:0;padding:0}
html,body{width:1200px;height:2360px;overflow:hidden}
body{background:var(--white);font-family:"Open Sans",Arial,sans-serif;color:var(--ink);position:relative}
.wrap{width:1160px;margin:0 auto;position:relative}

/* header */
.site-header{height:150px;position:relative}
.brand{position:absolute;left:20px;top:40px;display:flex;align-items:center;gap:14px}
.brand-dot{width:44px;height:44px;border-radius:50%;background:var(--teal)}
.brand-name{font-family:"Open Sans",Arial,sans-serif;font-weight:700;font-size:38px;color:var(--teal);letter-spacing:-.5px}
.account{position:absolute;right:20px;top:28px;width:420px}
.account-row{display:flex;gap:8px;margin-bottom:10px}
.field{height:34px;border:1px solid #bfc7cf;background:#fff;font-size:13px;color:#777;padding:0 10px;display:flex;align-items:center;flex:1}
.btn-blue{background:var(--blue);color:#fff;font-size:13px;font-weight:700;height:34px;padding:0 16px;display:flex;align-items:center}

/* nav */
.main-nav{background:var(--nav);height:50px}
.main-nav ul{list-style:none;display:flex;height:50px;width:1160px;margin:0 auto}
.main-nav li{color:#e8e8e8;font-size:14px;font-weight:600;text-transform:uppercase;padding:0 18px;display:flex;align-items:center}
.main-nav li.active{background:var(--nav-active)}

/* hero */
.hero{height:590px;position:relative;background:linear-gradient(120deg,#5a6470 0%,#8c96a0 40%,#c9b8a4 75%,#6f7882 100%)}
.hero-caption{position:absolute;left:20px;top:410px;width:760px;background:rgba(31,122,82,.9);padding:18px 26px;font-family:"PT Serif",Georgia,serif;font-size:38px;line-height:1.25;color:#fff}
.hero-arrows{position:absolute;left:800px;top:440px;display:flex;flex-direction:column;gap:10px}
.hero-arrows span{width:36px;height:36px;background:rgba(0,0,0,.5);display:flex;align-items:center;justify-content:center}

/* section titles */
.section-title{display:flex;align-items:center;gap:18px;font-family:"PT Serif",Georgia,serif;font-size:20px;text-transform:uppercase;letter-spacing:1px;color:#444}
.section-title::before,.section-title::after{content:"";flex:1;height:1px;background:var(--rule)}
.events{margin-top:40px}
.slider-dots{position:absolute;right:0;top:30px;display:flex;gap:6px}
.slider-dots span{width:26px;height:26px;border-radius:50%;background:var(--green);display:flex;align-items:center;justify-content:center}

.event-grid{display:flex;gap:40px;margin-top:50px}
.event{width:360px}
.event-photo{height:200px}
.event h3{font-family:"PT Serif",Georgia,serif;font-weight:400;font-size:26px;text-transform:uppercase;margin:30px 0 14px;color:#333}
.event p{font-size:14px;line-height:1.6;color:var(--muted)}
.btn-more{display:inline-flex;align-items:center;gap:6px;margin-top:24px;background:var(--green);color:#fff;font-size:13px;font-weight:700;padding:8px 18px;border-radius:16px;text-transform:uppercase}

/* news + join */
.lower{display:flex;gap:40px;margin-top:70px}
.col{flex:1}
.col .section-title{margin-bottom:40px}
.item{display:flex;gap:24px;margin-bottom:44px}
.round-photo{width:150px;height:150px;border-radius:50%;flex:none}
.square-photo{width:140px;height:150px;flex:none}
.item h4{font-family:"PT Serif",Georgia,serif;font-weight:700;font-size:17px;margin-bottom:6px;color:#333}
.item .role{font-size:13px;color:var(--muted);margin-bottom:8px}
.item .role b{color:var(--green);font-weight:600}
.item p{font-size:13px;line-height:1.6;color:var(--muted)}
.item .more{display:block;margin-top:12px;font-size:13px;color:var(--link)}

/* footer */
.site-footer{position:absolute;left:0;top:1880px;width:1200px;height:480px;background:var(--footer)}
.footer-cols{display:flex;gap:30px;width:1160px;margin:0 auto;padding-top:30px}
.footer-cols > div{flex:1}
.footer-cols h5{color:#eee;font-size:13px;font-weight:700;text-transform:uppercase;margin-bottom:18px}
.footer-cols p{color:var(--footer-text);font-size:13px;line-height:1.7;margin-bottom:14px}
.post{display:flex;gap:12px;margin-bottom:16px}
.post-thumb{width:56px;height:56px;flex:none}
.post p{margin:0;font-size:12px;line-height:1.5}
.quick{list-style:none}
.quick li{color:var(--link);font-size:13px;padding:5px 0;display:flex;gap:8px;align-items:center}
.quick li::before{content:"";width:6px;height:6px;border-radius:50%;background:var(--link)}
.ff{background:#2f2f2f;height:34px;margin-bottom:10px;color:#888;font-size:13px;padding:0 10px;display:flex;align-items:center}
.ff.tall{height:100px;align-items:flex-start;padding-top:8px}
.footer-base{position:absolute;left:0;bottom:0;width:1200px;height:80px;background:var(--footer-base);display:flex;align-items:center;justify-content:space-between;padding:0 20px}
.footer-base small{color:#777;font-size:12px}
.social{display:flex;gap:10px}
.social span{width:34px;height:34px;border-radius:50%;background:var(--blue)}
</style>
</head>
<body>

<header class="site-header">
  <div class="brand"><span class="brand-dot"></span><span class="brand-name">Gearline Tool Guild</span></div>
  <div class="account">
    <div class="account-row"><div class="field">Email</div><div class="field">Password</div><div class="btn-blue">LOGIN</div></div>
    <div class="account-row"><div class="field">Search Our Website...</div><div class="btn-blue">SUBMIT</div></div>
  </div>
</header>

<nav class="main-nav">
  <ul>
    <li class="active">Home</li><li>About Us</li><li>Membership</li><li>GTG Members</li><li>GTG Events</li><li>Tech-Doc Library</li><li>Market Research</li><li>Hidden Files</li>
  </ul>
</nav>

<section class="hero" role="img" aria-label="Photo of a smiling mechanic in a workshop talking with a customer">
  <div class="hero-caption">Lorem ipsum dolor sit amet, conse ctetuer adipiscing elit, sed diam.</div>
  <div class="hero-arrows">
    <span><svg width="14" height="14" viewBox="0 0 14 14"><path d="M9 2 4 7l5 5" stroke="#fff" stroke-width="2" fill="none"/></svg></span>
    <span><svg width="14" height="14" viewBox="0 0 14 14"><path d="M5 2l5 5-5 5" stroke="#fff" stroke-width="2" fill="none"/></svg></span>
  </div>
</section>

<main class="wrap">
  <section class="events">
    <h2 class="section-title">Industry Events</h2>
    <div class="slider-dots">
      <span><svg width="10" height="10" viewBox="0 0 10 10"><path d="M6.5 1.5 3 5l3.5 3.5" stroke="#fff" stroke-width="2" fill="none"/></svg></span>
      <span><svg width="10" height="10" viewBox="0 0 10 10"><path d="M3.5 1.5 7 5 3.5 8.5" stroke="#fff" stroke-width="2" fill="none"/></svg></span>
    </div>
    <div class="event-grid">
      <article class="event">
        <div class="event-photo" role="img" aria-label="Photo of two technicians inspecting a car tyre" style="background:linear-gradient(135deg,#2f3640,#7b8794)"></div>
        <h3>Parts Expo Show</h3>
        <p>Short summary of the show with dates, venue details and booth information for visiting members this year.</p>
        <span class="btn-more">Read More ›</span>
      </article>
      <article class="event">
        <div class="event-photo" role="img" aria-label="Photo of a technician fitting a wheel in a garage" style="background:linear-gradient(135deg,#2d4f8a,#8aa0c0)"></div>
        <h3>Custom Auto Show</h3>
        <p>Short summary of the show with dates, venue details and booth information for visiting members this year.</p>
        <span class="btn-more">Read More ›</span>
      </article>
      <article class="event">
        <div class="event-photo" role="img" aria-label="Photo of mechanics working beside a lifted car" style="background:linear-gradient(135deg,#4a4a52,#b09a86)"></div>
        <h3>Winter Tech Week 2015</h3>
        <p>Short summary of the show with dates, venue details and booth information for visiting members this year.</p>
        <span class="btn-more">Read More ›</span>
      </article>
    </div>
  </section>

  <div class="lower">
    <section class="col">
      <h2 class="section-title">Breaking News</h2>
      <article class="item">
        <div class="round-photo" role="img" aria-label="Photo of a person at a laptop" style="background:linear-gradient(135deg,#3c3c44,#9a9aa4)"></div>
        <div><h4>Hacking: It's Everybody's concern</h4><p>Short summary of the article covering key points for shop owners and technicians across the industry.</p><span class="more">Read More »</span></div>
      </article>
      <article class="item">
        <div class="round-photo" role="img" aria-label="Photo of a car engine bay under repair" style="background:linear-gradient(135deg,#1e2430,#5d6a80)"></div>
        <div><h4>Meeting the Needs of OEM Repairs</h4><p>Short summary of the article covering key points for shop owners and technicians across the industry.</p><span class="more">Read More »</span></div>
      </article>
    </section>
    <section class="col">
      <h2 class="section-title">Join GTG</h2>
      <article class="item">
        <div class="square-photo" role="img" aria-label="Photo of a technician beside a vehicle" style="background:linear-gradient(135deg,#5a5048,#b8a896)"></div>
        <div><h4>Lorem Ipsum</h4><div class="role">Department Executive - <b>View Full Profile</b></div><p>Short profile of this member covering their role, their company and their years in the trade.</p></div>
      </article>
      <article class="item">
        <div class="square-photo" role="img" aria-label="Photo of a workshop interior with equipment" style="background:linear-gradient(135deg,#6a5a4a,#c4b4a0)"></div>
        <div><h4>Lorem Ipsum</h4><div class="role">Department Executive - <b>View Full Profile</b></div><p>Short profile of this member covering their role, their company and their years in the trade.</p></div>
      </article>
    </section>
  </div>
</main>

<footer class="site-footer">
  <div class="footer-cols">
    <div>
      <h5>Company Details</h5>
      <p>Short notes on the institute, its members and mission for the tool and equipment trade.</p>
      <p>Gearline Tool Guild<br>120 Harbor Lane, Suite 4<br>Springfield, ST 00000</p>
      <p>Tel: 555 0100 200<br>info@gearline.example</p>
    </div>
    <div>
      <h5>Latest Blog Posts</h5>
      <div class="post"><div class="post-thumb" role="img" aria-label="Blog thumbnail photo" style="background:#555"></div><p>Short post title goes here today<br>Posted 12 March</p></div>
      <div class="post"><div class="post-thumb" role="img" aria-label="Blog thumbnail photo" style="background:#4a5560"></div><p>Short post title goes here today<br>Posted 12 March</p></div>
      <div class="post"><div class="post-thumb" role="img" aria-label="Blog thumbnail photo" style="background:#5a5048"></div><p>Short post title goes here today<br>Posted 12 March</p></div>
    </div>
    <div>
      <h5>Quick Links</h5>
      <ul class="quick"><li>Member benefits</li><li>About the guild</li><li>Upcoming events</li><li>Technical library</li><li>Market reports</li><li>News archive</li><li>Contact office</li></ul>
    </div>
    <div>
      <h5>Contact Us</h5>
      <div class="ff">Name</div><div class="ff">Email</div><div class="ff tall">Message</div>
      <div class="btn-blue" style="display:inline-flex">SUBMIT</div>
    </div>
  </div>
  <div class="footer-base">
    <small>Copyright © 2015 Gearline Tool Guild — All Rights Reserved</small>
    <div class="social"><span></span><span></span><span></span><span></span><span></span></div>
  </div>
</footer>

</body>
</html>
```